Market online tutoring + Back to School + give Support for students school work K to 12 Grade

To promote my tutoring business online need to create a two sided flyer. Need to get the attention of parents and educators who looking for help to support the digital learning of their students due to COVID-19 lock down. I need to project and differentiate that we offer support for online school with individualized learning . We tutor Elementary to High school students on all subjects you may take a look at my website qnacademyga.com for additional info and also I can provide
Updates

Hi All Due to Covid, we were unable to work on this project on time as originally planned. We were given an extension until March 15 and we will complete it by then. Sorry for any inconvenience and Thank you for your support. -QN Academy

Target Market(s)

Parents and students

Industry/Entity Type

Education

Requirements
Must have
• For online less fine print on the first page. The phone number and support text message. Back to School , Support Online learning KEV/NUR test prep should have some focus
Nice to have
• Discuss the platform We created a platform with live instructor interaction, virtual classroom, instructional videos, assessments, and practice to support every individual student’s need. We are confident in our ability to provide the most effective distance learning experience.
Should not have
• too much clunky and packed with content. Should be easy to read with color

```html
<!DOCTYPE html>
<html lang="en">
<head>
<meta charset="utf-8">
<title>QN Academy – Online Tutoring Flyer</title>
<link rel="stylesheet" href="https://fonts.googleapis.com/css2?family=Oswald:wght@500;600&family=Lato:ital,wght@0,400;0,700;1,700&display=swap">
<style>
:root{
  --red:#d62b2b;
  --navy:#0f3a4f;
  --ink:#1d1d1d;
  --panel:#e6e6e8;
  --backdrop:#4a4a4a;
  --white:#ffffff;
}
*{margin:0;padding:0;box-sizing:border-box}
html,body{width:1200px;height:1200px;overflow:hidden;background:var(--backdrop)}
body{position:relative;font-family:"Lato",sans-serif;color:var(--ink)}
.flyer{position:absolute;top:202px;width:562px;height:788px;background:var(--white);overflow:hidden;box-shadow:0 6px 14px rgba(0,0,0,.35)}
.flyer--front{left:30px}
.flyer--back{left:610px}
.abs{position:absolute}
.shapes{position:absolute;left:0;top:0}
.display{font-family:"Oswald",sans-serif;font-weight:600;display:inline-block;white-space:nowrap;transform:scaleX(.82);transform-origin:left top}
.brand{display:flex;align-items:center;gap:12px}
.brand__mark{background:var(--navy)}
.brand__name{font-family:"Lato",sans-serif;font-weight:700;color:var(--navy);letter-spacing:1px}
.photo{position:absolute}
/* front */
.hero__title{left:24px;top:146px;color:var(--white);line-height:66px;font-size:68px}
.hero__sub{left:24px;top:278px;color:var(--white);font-size:32px;font-weight:500;line-height:1}
.hero__band{left:20px;top:338px;color:var(--white);font-size:27px;font-weight:500;line-height:1}
.hero__band small{font-size:17px}
.intro{left:19px;top:392px;width:300px;font-size:11.2px;line-height:13.5px;color:var(--red);font-weight:700}
.intro .navy{color:var(--navy)}
.checks{left:26px;top:468px;list-style:none;font-size:12px;line-height:22px;color:var(--ink)}
.checks li{display:flex;align-items:center;gap:6px}
.section-title{color:var(--red);font-size:23px;font-weight:500;line-height:1}
.who__title{left:22px;top:542px}
.who__text{left:22px;top:588px;width:308px;font-size:9.6px;line-height:12px}
.love__title{left:364px;top:388px}
.love__quote{left:364px;top:418px;width:195px;font-style:italic;font-weight:700;font-size:14px;line-height:18px;color:var(--navy)}
.love__quote small{font-style:normal;font-size:9px;font-weight:700}
.success__panel{left:350px;top:464px;width:212px;height:273px;background:var(--panel)}
.success__photo{left:358px;top:471px;width:196px;height:125px;border:3px solid var(--navy);background:linear-gradient(135deg,#c7a692,#8f9aa6 55%,#e9ecef)}
.success__title{left:360px;top:602px;font-size:27px;line-height:31px;color:var(--red);font-weight:500}
.success__rule{left:360px;top:666px;width:40px;height:2px;background:var(--navy)}
.success__text{left:360px;top:672px;width:194px;font-size:9.6px;line-height:12px;text-align:justify}
.footer__phone{left:20px;top:716px;display:flex;align-items:center;gap:6px;color:var(--white);font-size:27px;font-weight:500;line-height:1}
.footer__phone svg{flex:none}
.footer__web{left:22px;top:752px;display:flex;align-items:center;gap:8px;color:var(--white);font-size:13px;letter-spacing:1.6px}
.footer__addr{left:208px;top:749px;display:flex;gap:7px;color:var(--white);font-size:8.8px;line-height:11px}
.footer__mail{left:382px;top:755px;display:flex;gap:6px;align-items:center;color:var(--white);font-size:8.8px}
/* back */
.feature__title{left:56px;color:var(--red);font-size:15.5px;font-weight:400;letter-spacing:.2px}
.feature__text{left:56px;width:267px;font-size:10.2px;line-height:13px;text-align:justify}
.closing{left:28px;top:641px;width:292px;font-size:10.2px;line-height:13.4px;font-weight:700;color:var(--navy)}
.closing em{font-style:normal;color:var(--red)}
.services__panel{left:345px;top:345px;width:217px;height:392px;background:var(--panel)}
.services__title{left:362px;top:350px}
.services__rule{left:362px;top:380px;width:55px;height:2px;background:var(--navy)}
.services__list{left:362px;top:390px;width:195px;list-style:none;font-size:11.2px;font-weight:700;color:var(--ink)}
.services__list li{display:flex;gap:6px;margin-bottom:9px;line-height:14px}
.services__list svg{flex:none;margin-top:2px}
</style>
</head>
<body>

<!-- FRONT -->
<section class="flyer flyer--front">
  <div class="photo" style="left:240px;top:130px;width:322px;height:248px;background:linear-gradient(120deg,#e8eef2 0%,#c9d3da 40%,#3b2a22 85%)" role="img" aria-label="Young boy wearing a face mask sitting at a desk with a laptop and coloured pencils"></div>
  <svg class="shapes" width="562" height="788" aria-hidden="true">
    <polygon points="0,130 234,130 262,329 0,329" fill="#d62b2b"/>
    <polygon points="0,329 262,329 282,378 0,378" fill="#0f3a4f"/>
    <rect x="180" y="737" width="382" height="51" fill="#d62b2b"/>
    <polygon points="0,710 178,710 200,788 0,788" fill="#0f3a4f"/>
  </svg>

  <div class="brand abs" style="left:160px;top:34px">
    <div class="brand__mark" style="width:62px;height:62px"></div>
    <div class="brand__name" style="font-size:30px">QN ACADEMY</div>
  </div>

  <h1 class="hero__title abs display">ONLINE<br>TUTORING</h1>
  <div class="hero__sub abs display">for students K to 12</div>
  <div class="hero__band abs display"><small>DUE TO</small> COVID-19 LOCKDOWN</div>

  <p class="intro abs">Due to CoVid-19 Lockdown we offer individually tailored courses in online to meet varying needs of students, <span class="navy">whether it is a one-on-one tutoring or special subject tutoring; QN Academy has experienced teachers to help you in any academic subject.</span></p>

  <ul class="checks abs">
    <li><svg width="14" height="14" viewBox="0 0 14 14"><circle cx="7" cy="7" r="6" fill="none" stroke="#d62b2b" stroke-width="1.3"/><path d="M3.8 7.2l2.2 2.2 5-5.6" fill="none" stroke="#d62b2b" stroke-width="1.6"/></svg>One-one-one online tutoring</li>
    <li><svg width="14" height="14" viewBox="0 0 14 14"><circle cx="7" cy="7" r="6" fill="none" stroke="#d62b2b" stroke-width="1.3"/><path d="M3.8 7.2l2.2 2.2 5-5.6" fill="none" stroke="#d62b2b" stroke-width="1.6"/></svg>Online Accelerated programs</li>
    <li><svg width="14" height="14" viewBox="0 0 14 14"><circle cx="7" cy="7" r="6" fill="none" stroke="#d62b2b" stroke-width="1.3"/><path d="M3.8 7.2l2.2 2.2 5-5.6" fill="none" stroke="#d62b2b" stroke-width="1.6"/></svg>Tutoring for Science, Social Studies and Others</li>
  </ul>

  <h2 class="who__title abs section-title display">WHO ARE WE</h2>
  <p class="who__text abs">QN Academy in Alderton/Brookfield Georgia, we are a private Tutoring center which provides group coaching in Math, Reading, KEV Preparation and Computer Programming for kids. We are proud to offer a curriculum that is truly unique, providing a strong focus on advanced coaching in Math and Reading. We also provide effective coaching for standardized tests like KEV and MVTS etc. We step away from the regular coaching method and implement effective problem solving techniques and critical thinking skills to help achieve stronger academic results.</p>

  <h2 class="love__title abs section-title display">We Love Teaching</h2>
  <p class="love__quote abs">"Teaching is the greatest act of optimism" <small>- DANA WHITFIELD</small></p>

  <div class="success__panel abs"></div>
  <div class="success__photo abs" role="img" aria-label="Girl writing in a notebook while her teacher appears on a laptop screen"></div>
  <h2 class="success__title abs display">Students' Success is<br>Our Success !</h2>
  <div class="success__rule abs"></div>
  <p class="success__text abs">QN Academy provides every student with personal guidance. We give students the platform and tools needed to conquer, to build confidence in them, to excel in their goals, and to achieve their dreams.</p>

  <div class="footer__phone abs"><svg width="18" height="18" viewBox="0 0 18 18"><circle cx="9" cy="9" r="8" fill="none" stroke="#fff" stroke-width="1.4"/><path d="M6 5.2c.6-.4 1.1-.3 1.4.3l.6 1.2c.2.5 0 .8-.4 1.1.5 1.1 1.2 1.8 2.3 2.3.3-.4.7-.6 1.1-.4l1.2.6c.6.3.7.8.3 1.4-1.3 1.6-6.9-2.5-6.5-6.5z" fill="#fff"/></svg><span class="display" style="font-weight:500">555-014-2237</span></div>
  <div class="footer__web abs"><svg width="13" height="13" viewBox="0 0 14 14"><circle cx="7" cy="7" r="6" fill="none" stroke="#fff" stroke-width="1.2"/><ellipse cx="7" cy="7" rx="2.6" ry="6" fill="none" stroke="#fff" stroke-width="1"/><path d="M1 7h12" stroke="#fff"/></svg>qnacademyga.com</div>
  <div class="footer__addr abs"><svg width="11" height="15" viewBox="0 0 11 15"><path d="M5.5 0C2.5 0 0 2.4 0 5.4 0 9.3 5.5 15 5.5 15S11 9.3 11 5.4C11 2.4 8.5 0 5.5 0z" fill="#fff"/><circle cx="5.5" cy="5.3" r="2" fill="#d62b2b"/></svg><span>4420 Maple Brook Rd, Suite 210<br>Alderton, GA 30099</span></div>
  <div class="footer__mail abs"><svg width="12" height="9" viewBox="0 0 12 9"><rect width="12" height="9" fill="#fff"/><path d="M0 0l6 5 6-5" fill="none" stroke="#d62b2b" stroke-width="1"/></svg>hello@qnacademyga.com</div>
</section>

<!-- BACK -->
<section class="flyer flyer--back">
  <div class="photo" style="left:0;top:22px;width:562px;height:320px;background:linear-gradient(110deg,#d9dde2 0%,#b9c2cb 35%,#6b4a45 65%,#c9ccd0 100%)" role="img" aria-label="Teenage boy in a plaid shirt studying at a desk with a laptop"></div>
  <svg class="shapes" width="562" height="788" aria-hidden="true">
    <polygon points="0,0 562,0 562,22 295,22 215,93 0,93" fill="#fff"/>
    <polyline points="0,93 215,93 295,22 562,22" fill="none" stroke="#d62b2b" stroke-width="4"/>
    <line x1="34" y1="384" x2="34" y2="554" stroke="#0f3a4f" stroke-width="1" stroke-dasharray="2 2"/>
    <g>
      <circle cx="34" cy="370" r="15" fill="#d62b2b"/><circle cx="34" cy="370" r="12" fill="#0f3a4f"/>
      <rect x="29" y="364" width="9" height="11" fill="none" stroke="#fff" stroke-width="1.4"/>
      <circle cx="34" cy="468" r="15" fill="#d62b2b"/><circle cx="34" cy="468" r="12" fill="#0f3a4f"/>
      <circle cx="33" cy="467" r="4" fill="none" stroke="#fff" stroke-width="1.5"/><line x1="36" y1="470" x2="40" y2="474" stroke="#fff" stroke-width="1.6"/>
      <circle cx="34" cy="566" r="15" fill="#d62b2b"/><circle cx="34" cy="566" r="12" fill="#0f3a4f"/>
      <path d="M29 572l5-12 5 12M31 568h6" fill="none" stroke="#fff" stroke-width="1.5"/>
    </g>
    <rect x="0" y="737" width="562" height="51" fill="#d62b2b"/>
    <polygon points="0,710 178,710 200,788 0,788" fill="#0f3a4f"/>
  </svg>

  <div class="brand abs" style="left:22px;top:30px;gap:10px">
    <div class="brand__mark" style="width:46px;height:46px"></div>
    <div class="brand__name" style="font-size:22px">QN ACADEMY</div>
  </div>

  <h3 class="feature__title abs" style="top:360px">TEST PREPARATION</h3>
  <p class="feature__text abs" style="top:388px">We provide specialized and effective test preparation courses in KEV. " Practice Makes Perfect". We get students into a routine of consistent practice of various concepts required for success on the KEV test.</p>

  <h3 class="feature__title abs" style="top:459px">CRITICAL THINKING</h3>
  <p class="feature__text abs" style="top:487px">We provide excellent critical and analytical thinking practice. Our program also helps students develop valuable tools to properly prepare for standardized tests like RDAT, MVTS, etc.</p>

  <h3 class="feature__title abs" style="top:557px">ADVANCED ACADEMIC COACHING</h3>
  <p class="feature__text abs" style="top:582px">We offer advanced coaching in all academic subjects for grade 1 to grade 12. Our Mathematics and Language Arts courses follow common core standards.</p>

  <p class="closing abs">QN Academy will be able to provide the service you need to <em>"Excel your Goals and Achieve"</em>. Do you have different need other than our standard offerings? Please contact us we will customize our offerings to meet your need.</p>

  <div class="services__panel abs"></div>
  <h2 class="services__title abs section-title display">OUR SERVICES</h2>
  <div class="services__rule abs"></div>
  <ul class="services__list abs">
    <li><svg width="11" height="11" viewBox="0 0 12 12"><circle cx="6" cy="6" r="5.2" fill="none" stroke="#333" stroke-width="1"/><path d="M3.4 6.1l1.8 1.8 3.6-3.9" fill="none" stroke="#333" stroke-width="1.2"/></svg>Mathematics (Georgia Standard of Education)</li>
    <li><svg width="11" height="11" viewBox="0 0 12 12"><circle cx="6" cy="6" r="5.2" fill="none" stroke="#333" stroke-width="1"/><path d="M3.4 6.1l1.8 1.8 3.6-3.9" fill="none" stroke="#333" stroke-width="1.2"/></svg>Reading (GSE)</li>
    <li><svg width="11" height="11" viewBox="0 0 12 12"><circle cx="6" cy="6" r="5.2" fill="none" stroke="#333" stroke-width="1"/><path d="M3.4 6.1l1.8 1.8 3.6-3.9" fill="none" stroke="#333" stroke-width="1.2"/></svg>Writing (GSE)</li>
    <li><svg width="11" height="11" viewBox="0 0 12 12"><circle cx="6" cy="6" r="5.2" fill="none" stroke="#333" stroke-width="1"/><path d="M3.4 6.1l1.8 1.8 3.6-3.9" fill="none" stroke="#333" stroke-width="1.2"/></svg>KEV Preparation</li>
    <li><svg width="11" height="11" viewBox="0 0 12 12"><circle cx="6" cy="6" r="5.2" fill="none" stroke="#333" stroke-width="1"/><path d="M3.4 6.1l1.8 1.8 3.6-3.9" fill="none" stroke="#333" stroke-width="1.2"/></svg>Critical Thinking</li>
    <li><svg width="11" height="11" viewBox="0 0 12 12"><circle cx="6" cy="6" r="5.2" fill="none" stroke="#333" stroke-width="1"/><path d="M3.4 6.1l1.8 1.8 3.6-3.9" fill="none" stroke="#333" stroke-width="1.2"/></svg>Computer Science</li>
    <li><svg width="11" height="11" viewBox="0 0 12 12"><circle cx="6" cy="6" r="5.2" fill="none" stroke="#333" stroke-width="1"/><path d="M3.4 6.1l1.8 1.8 3.6-3.9" fill="none" stroke="#333" stroke-width="1.2"/></svg>Robotics</li>
    <li><svg width="11" height="11" viewBox="0 0 12 12"><circle cx="6" cy="6" r="5.2" fill="none" stroke="#333" stroke-width="1"/><path d="M3.4 6.1l1.8 1.8 3.6-3.9" fill="none" stroke="#333" stroke-width="1.2"/></svg>Custom Courses</li>
  </ul>
  <div class="photo" style="left:380px;top:585px;width:150px;height:152px;background:radial-gradient(ellipse at 50% 40%,#7a5038 0%,#2f4f55 55%,#e6e6e8 80%)" role="img" aria-label="Smiling woman working on a laptop"></div>

  <div class="footer__phone abs"><svg width="18" height="18" viewBox="0 0 18 18"><circle cx="9" cy="9" r="8" fill="none" stroke="#fff" stroke-width="1.4"/><path d="M6 5.2c.6-.4 1.1-.3 1.4.3l.6 1.2c.2.5 0 .8-.4 1.1.5 1.1 1.2 1.8 2.3 2.3.3-.4.7-.6 1.1-.4l1.2.6c.6.3.7.8.3 1.4-1.3 1.6-6.9-2.5-6.5-6.5z" fill="#fff"/></svg><span class="display" style="font-weight:500">555-014-2237</span></div>
  <div class="footer__web abs"><svg width="13" height="13" viewBox="0 0 14 14"><circle cx="7" cy="7" r="6" fill="none" stroke="#fff" stroke-width="1.2"/><ellipse cx="7" cy="7" rx="2.6" ry="6" fill="none" stroke="#fff" stroke-width="1"/><path d="M1 7h12" stroke="#fff"/></svg>qnacademyga.com</div>
  <div class="footer__addr abs"><svg width="11" height="15" viewBox="0 0 11 15"><path d="M5.5 0C2.5 0 0 2.4 0 5.4 0 9.3 5.5 15 5.5 15S11 9.3 11 5.4C11 2.4 8.5 0 5.5 0z" fill="#fff"/><circle cx="5.5" cy="5.3" r="2" fill="#d62b2b"/></svg><span>4420 Maple Brook Rd, Suite 210<br>Alderton, GA 30099</span></div>
  <div class="footer__mail abs"><svg width="12" height="9" viewBox="0 0 12 9"><rect width="12" height="9" fill="#fff"/><path d="M0 0l6 5 6-5" fill="none" stroke="#d62b2b" stroke-width="1"/></svg>hello@qnacademyga.com</div>
</section>

</body>
</html>
```